7 page website for Dog Training Business

we are seeking a website design that should be 7 pages for a Las Vegas Dog training business. the site will have a heavy focus on video, and social media. Ideas design can be borrowed from http://plumcrestway.net
attached is a copy of the logo and business card mock up. Content is currently being written and will be posted shortly

Training

```html
<!DOCTYPE html>
<html lang="en">
<head>
<meta charset="utf-8">
<title>Brindle Paws Dog Training</title>
<link rel="stylesheet" href="https://fonts.googleapis.com/css2?family=Oswald:wght@400;500&family=Open+Sans:ital,wght@0,400;0,700;1,400&display=swap">
<style>
:root{
  --green:#b5cc45;
  --green-light:#c5da56;
  --green-dark:#8fa62d;
  --pink:#e8626a;
  --brown:#6b4a2e;
  --nav-bg:#eeeeee;
  --text:#555555;
  --white:#ffffff;
}
*{box-sizing:border-box;margin:0;padding:0}
html,body{width:809px;height:1200px;overflow:hidden}
body{position:relative;background:var(--white);font-family:"Open Sans",Arial,sans-serif;color:var(--text)}
.abs{position:absolute}
.hero-bg{left:0;top:0;width:809px;height:430px;background:linear-gradient(180deg,#4e6fc9 0%,#7b97d8 45%,#a9b9d4 70%,#cdd5c3 100%)}
.top-rule{left:0;top:0;width:809px;height:4px;background:var(--green)}
.brand{left:108px;top:20px;width:78px;height:78px;border-radius:50%;background:var(--green);border:4px solid var(--white);display:flex;align-items:center;justify-content:center;text-align:center;font-family:"Oswald",sans-serif;font-weight:500;font-size:15px;line-height:1.05;color:var(--brown)}
.contact-bar{right:263px;top:70px;font-family:"Oswald",sans-serif;font-size:10px;letter-spacing:1px;color:var(--white);display:flex;align-items:center;gap:5px;white-space:nowrap}
.socials{left:556px;top:67px;display:flex;gap:5px}
.socials span{width:20px;height:20px;border-radius:2px}
.nav{left:99px;top:115px;width:609px;height:47px;background:var(--nav-bg);display:flex}
.nav a{flex:auto;border-right:1px solid #d6d6d6;display:flex;flex-direction:column;align-items:center;justify-content:center;gap:5px;text-decoration:none;font-family:"Oswald",sans-serif;font-size:9.5px;letter-spacing:1.5px;color:var(--brown)}
.nav a:last-child{border-right:0}
.nav i{width:8px;height:8px;border-radius:50%;background:var(--green)}
.video-panel{left:99px;top:162px;width:407px;height:228px;background:var(--green)}
.video-title{left:118px;top:180px;font-family:"Oswald",sans-serif;font-size:20px;letter-spacing:1px;color:var(--white);display:flex;align-items:center;gap:8px}
.video-player{left:108px;top:218px;width:390px;height:163px;background:linear-gradient(180deg,#3a3530,#6b6258 60%,#2a2624)}
.video-caption{left:113px;top:221px;font-size:8px;color:var(--white)}
.video-controls{left:108px;top:367px;width:390px;height:14px;background:#1b1b1b}
.play-btn{left:286px;top:287px;width:36px;height:26px;border-radius:4px;background:rgba(0,0,0,.7)}
.video-list{left:506px;top:162px;width:202px;height:228px;background:var(--green-dark)}
.video-item{position:absolute;left:506px;width:202px;height:39px;display:flex;align-items:center;justify-content:flex-end;gap:6px;padding-right:6px}
.video-item.active{background:var(--pink)}
.video-item .txt{text-align:right;font-size:7.5px;line-height:1.4}
.video-item b{display:block;color:var(--white);font-size:7.5px}
.video-item em{font-style:normal;color:var(--brown)}
.video-item .thumb{width:40px;height:30px;background:linear-gradient(135deg,#5a4a3a,#a08866);border:1px solid var(--white)}
.testimonials{left:99px;top:440px;width:609px;display:flex;gap:30px;padding:0 20px}
.quote{flex:1;font-style:italic;font-size:9px;line-height:1.45;color:#666}
.quote .mark{color:var(--green);font-weight:700;font-style:normal}
.quote .by{display:block;margin-top:8px;font-style:normal;font-size:9.5px;color:var(--green)}
.slider{left:99px;top:557px;width:609px;height:153px;background:linear-gradient(180deg,#2e4d2a 0%,#5f8b3e 50%,#2b4326 100%)}
.slide-caption{left:99px;top:690px;width:609px;height:20px;background:rgba(0,0,0,.45);color:var(--white);font-family:"Oswald",sans-serif;font-size:9px;letter-spacing:1.5px;text-align:right;padding:4px 8px}
.gallery-link{left:99px;top:710px;width:609px;height:20px;background:var(--pink);color:var(--white);font-family:"Oswald",sans-serif;font-size:9px;letter-spacing:1.5px;display:flex;align-items:center;justify-content:center;gap:6px}
.column{top:757px;width:268px}
.column h2{font-family:"Oswald",sans-serif;font-weight:400;font-size:17px;letter-spacing:1px;color:var(--brown);display:flex;align-items:center;gap:8px;margin-bottom:14px;white-space:nowrap}
.column .body{font-size:7.4px;line-height:1.62;text-align:justify;color:#666;overflow:hidden}
.column .pic{float:left;width:78px;height:78px;border-radius:50%;background:radial-gradient(circle at 40% 40%,#b58a5a,#6b7f3a);margin:2px 12px 4px 2px}
.col-divider{left:402px;top:748px;width:1px;height:215px;background:#ddd}
.footer{left:99px;top:980px;width:609px;height:190px;background:var(--green-light)}
.footer-brand{left:207px;top:997px;width:103px;height:103px;border-radius:50%;background:var(--green);border:5px solid var(--white);display:flex;align-items:center;justify-content:center;text-align:center;font-family:"Oswald",sans-serif;font-weight:500;font-size:19px;line-height:1.05;color:var(--brown)}
.footer-info{left:160px;top:1110px;font-size:7.5px;line-height:1.7;color:var(--white)}
.footer-info .addr{font-weight:700}
.footer-info p{display:flex;align-items:center;gap:6px}
.footer-info .sub{padding-left:40px}
.map{left:411px;top:996px;width:275px;height:158px;background:linear-gradient(135deg,#e9e4d6,#d8dcc6 50%,#e6d9b8);border:1px solid #cfd3b0}
</style>
</head>
<body>
<div class="abs hero-bg" role="img" aria-label="Outdoor photo of dogs in a park under a blue sky"></div>
<div class="abs top-rule"></div>

<div class="abs brand">Brindle<br>Paws</div>

<div class="abs contact-bar">
  <svg width="10" height="10" viewBox="0 0 24 24"><path fill="#fff" d="M6.6 10.8a15 15 0 0 0 6.6 6.6l2.2-2.2c.3-.3.7-.4 1-.2 1.1.4 2.3.6 3.6.6.6 0 1 .4 1 1V20c0 .6-.4 1-1 1A17 17 0 0 1 3 4c0-.6.4-1 1-1h3.5c.6 0 1 .4 1 1 0 1.3.2 2.5.6 3.6.1.3 0 .7-.2 1z"/></svg>
  <span>1-555-0192 CONTACT US • FOLLOW US!</span>
</div>
<div class="abs socials">
  <span style="background:#3b5998"></span><span style="background:#dd4b39"></span><span style="background:#b31217"></span><span style="background:#517fa4"></span><span style="background:#ff0084"></span><span style="background:#1da1f2"></span>
</div>

<nav class="abs nav">
  <a><i></i>HOME</a><a><i></i>ABOUT</a><a><i></i>SERVICES / RATES</a><a><i></i>PHOTOS / VIDEOS</a><a><i></i>FAQ</a><a><i></i>TESTIMONIALS</a><a><i></i>PAW TIPS</a><a><i></i>STORE</a><a><i></i>CONTACT</a>
</nav>

<div class="abs video-panel"></div>
<div class="abs video-title">
  <svg width="20" height="14" viewBox="0 0 20 14"><rect width="20" height="14" rx="3" fill="#e8626a"/><path d="M8 4l5 3-5 3z" fill="#fff"/></svg>
  WATCH OUR VIDEOS!
</div>
<div class="abs video-player" role="img" aria-label="Video still of a trainer walking a small dog on a leash"></div>
<div class="abs video-caption">Leash Walk: Calm Down!</div>
<div class="abs play-btn"><svg width="36" height="26"><path d="M15 8l8 5-8 5z" fill="#fff"/></svg></div>
<div class="abs video-controls"><svg width="390" height="14"><path d="M6 4l6 3-6 3z" fill="#ccc"/><text x="40" y="10" font-size="7" fill="#ccc" font-family="Arial">0:00 / 3:44</text></svg></div>

<div class="abs video-list"></div>
<div class="video-item" style="top:172px"><div class="txt"><b>FIRST VIDEO LINK</b><em>This is a subtitle</em></div><div class="thumb" role="img" aria-label="Video thumbnail"></div></div>
<div class="video-item active" style="top:211px"><div class="txt"><b>ANOTHER VIDEO</b><em>sed ut labore et dolore m</em></div><div class="thumb" role="img" aria-label="Video thumbnail"></div></div>
<div class="video-item" style="top:250px"><div class="txt"><b>DO EIUSMOD TE</b><em>usmod tempor incid</em></div><div class="thumb" role="img" aria-label="Video thumbnail"></div></div>
<div class="video-item" style="top:289px"><div class="txt"><b>LOREM IPSUM DOLOR SIT AMET</b><em>m ad minim ip ex ea commodo</em></div><div class="thumb" role="img" aria-label="Video thumbnail"></div></div>
<div class="video-item" style="top:328px"><div class="txt"><b>SCING ELIT, SED</b><em>do consequat. Duis aute irure do</em></div><div class="thumb" role="img" aria-label="Video thumbnail"></div></div>

<section class="abs testimonials">
  <p class="quote"><span class="mark">“</span> Lorem ipsum dolor sit amet, consectetur adipiscing elit, sed do eiusmod tempor incididunt ut labore et dolore magna aliqua. Ut enim ad minim ip ex ea commodo consequat. Duis aute irure dolo <span class="mark">”</span><span class="by">- by John Doe</span></p>
  <p class="quote"><span class="mark">“</span> Lorem ipsum dolor sit amet, consectetur adipiscing elimod tempor incididunt ut labore et dolore magna aliqua. Ut enim ad minim ip ex ea commodo consequat. Duis aute irure dolo <span class="mark">”</span><span class="by">- by John Doe</span></p>
  <p class="quote"><span class="mark">“</span> Lorem ipsum dolor sit amet, consectetur adipiscing por incididunt ut labore et dolore magna aliqua. Ut enim ad minim ip ex ea commodo consequat. Duis aute irure dolo <span class="mark">”</span><span class="by">- by John Doe</span></p>
</section>

<div class="abs slider" role="img" aria-label="Photo of a dog running across grass with a ball"></div>
<svg class="abs" style="left:137px;top:625px" width="12" height="16"><path d="M10 2L3 8l7 6" stroke="#fff" stroke-width="2" fill="none" opacity=".8"/></svg>
<svg class="abs" style="left:657px;top:625px" width="12" height="16"><path d="M2 2l7 6-7 6" stroke="#fff" stroke-width="2" fill="none" opacity=".8"/></svg>
<div class="abs slide-caption">YET ANOTHER CAPTION</div>
<div class="abs gallery-link"><svg width="8" height="8"><rect width="8" height="8" rx="2" fill="#fff" opacity=".7"/></svg>LINK TO A PHOTO GALLERY</div>

<article class="abs column" style="left:120px">
  <h2><svg width="14" height="14" viewBox="0 0 14 14" fill="#6b4a2e"><ellipse cx="7" cy="9.5" rx="3.5" ry="3"/><circle cx="2.5" cy="5.5" r="1.5"/><circle cx="5" cy="2.5" r="1.5"/><circle cx="9" cy="2.5" r="1.5"/><circle cx="11.5" cy="5.5" r="1.5"/></svg>THIS IS A TEXT</h2>
  <div class="body"><div class="pic" role="img" aria-label="Photo of a dog sitting on grass with its trainer"></div>At vero eos et accusamus et iusto odio dignissimos ducimus qui blanditiis praesentium voluptatum deleniti atque corrupti quos dolores et quas molestias excepturi sint occaecati cupiditate non provident, similique sunt in culpa qui officia deserunt mollitia animi, id est laborum et dolorum fuga. Et harum quidem rerum facilis est et expedita distinctio. Nam libero tempore, cum soluta nobis est eligendi optio cumque nihil impedit quo est, omnis dolor repellendus. Temporibus autem quibusdam et aut officiis debitis aut rerum necessitatibus saepe eveniet ut et voluptates repudiandae sint et molestiae non recusandae. Itaque earum rerum hic tenetur a sapiente delectus, ut aut reiciendis voluptatibus maiores alias consequatur aut perferendis doloribus asperiores repellat.</div>
</article>
<div class="abs col-divider"></div>
<article class="abs column" style="left:412px">
  <h2><svg width="14" height="14" viewBox="0 0 14 14" fill="#6b4a2e"><ellipse cx="7" cy="9.5" rx="3.5" ry="3"/><circle cx="2.5" cy="5.5" r="1.5"/><circle cx="5" cy="2.5" r="1.5"/><circle cx="9" cy="2.5" r="1.5"/><circle cx="11.5" cy="5.5" r="1.5"/></svg>THIS IS ANOTHER TEXT</h2>
  <div class="body"><div class="pic" role="img" aria-label="Photo of a dog standing in a green field"></div>At vero eos et accusamus et iusto odio dignissimos ducimus qui blanditiis praesentium voluptatum deleniti atque corrupti quos dolores et quas molestias excepturi sint occaecati cupiditate non provident, similique sunt in culpa qui officia deserunt mollitia animi, id est laborum et doloruest, omnis dolor repellendus. Temporibus autem quibusdam et aut officiis debitis aut rerum necessitatibus saepe eveniet ut et voluptates tenetur a sapiente delectus, ut aut reiciendis voluptatibus maiores alias consequatur aut perferendis doloribus asperiores repellat.</div>
</article>

<footer class="abs footer"></footer>
<div class="abs footer-brand">Brindle<br>Paws</div>
<div class="abs footer-info">
  <p class="addr"><svg width="7" height="9" viewBox="0 0 10 14"><path d="M5 0a5 5 0 0 1 5 5c0 4-5 9-5 9S0 9 0 5a5 5 0 0 1 5-5z" fill="#6b4a2e"/></svg>4120 Marigold Lane, Las Vegas, NV, USA</p>
  <p class="sub"><svg width="8" height="8" viewBox="0 0 24 24"><path fill="#6b4a2e" d="M6.6 10.8a15 15 0 0 0 6.6 6.6l2.2-2.2c.3-.3.7-.4 1-.2 1.1.4 2.3.6 3.6.6.6 0 1 .4 1 1V20c0 .6-.4 1-1 1A17 17 0 0 1 3 4c0-.6.4-1 1-1h3.5c.6 0 1 .4 1 1 0 1.3.2 2.5.6 3.6.1.3 0 .7-.2 1z"/></svg>Telephone: +1 702-555-0140</p>
  <p class="sub"><svg width="8" height="8"><rect x="1" y="2" width="6" height="5" fill="#6b4a2e"/></svg>Fax: +1 702-555-0141</p>
  <p class="sub"><svg width="8" height="8"><rect x=".5" y="1.5" width="7" height="5" fill="none" stroke="#6b4a2e"/><path d="M.5 1.5l3.5 3 3.5-3" stroke="#6b4a2e" fill="none"/></svg>Email: hello@brindlepaws.com</p>
</div>
<div class="abs map" role="img" aria-label="Street map of Las Vegas showing the business location"></div>
</body>
</html>
```